Website - User Access Door - Images

4 separate images that fit together to form a door that I will animate to open up when a user accesses my website. 1. Left Door 2. Right Door. 3. Lock (open) 4. Lock (closed). High resolution as it must look good on huge monitors.

Attached is a picture very close to what I'm after. I guess the main thing to keep in mind is that it needs to look strong. The attached graphic is quite close to what I'm after, but I need a unique design, not a copy of this one.

Reason: I was promised more than 3 submissions by PixelHarbor. I guess they need more time...

Here are some images for inspiration. Think Soviet iron nuclear bunker door. Heavy, Strong (but latest technology incorporated)

http://img2.frambleweb.example/__cb20090716105544/zorvak/images/1/1d/KTRF_bunker_door.jpg

http://www.tobiasrendwerk.example/QPA_Bunker3_TobiasLendl.jpg

Nice texture ideas:
http://www.grainvault.example/data/media/8/steel_door_texture.jpg

Think games:
http://www.quillmapguides.example/korvane/zone7b/24.jpg

http://brisktray.example/wp-content/uploads/2013/09/Metal-Door-Wall-Graphic-Decals.jpg

```html
<!DOCTYPE html>
<html lang="en">
<head>
<meta charset="utf-8">
<title>User Access Door</title>
<style>
  :root {
    --void: #000000;
    --steel-dark: #111111;
    --steel-mid: #5a5a5a;
    --steel-light: #e8e8e8;
    --frame: #8a8a8a;
    --glow-green: #22e01a;
    --glow-red: #e01414;
    --tray: rgba(255, 255, 255, 0.22);
  }
  html, body {
    margin: 0;
    padding: 0;
    width: 1200px;
    height: 900px;
    overflow: hidden;
    background: var(--void);
  }
  .door-canvas {
    display: block;
    width: 1200px;
    height: 900px;
  }
</style>
</head>
<body>
<svg class="door-canvas" viewBox="0 0 1200 900" xmlns="http://www.w3.org/2000/svg">
  <defs>
    <linearGradient id="wall-sheen" x1="0" y1="0" x2="0" y2="1">
      <stop offset="0" stop-color="#000"/>
      <stop offset="0.5" stop-color="#fff"/>
      <stop offset="1" stop-color="#000"/>
    </linearGradient>
    <linearGradient id="wall-fade" x1="0" y1="0" x2="1" y2="0">
      <stop offset="0" stop-color="#000" stop-opacity="0"/>
      <stop offset="0.1" stop-color="#000" stop-opacity="1"/>
      <stop offset="0.9" stop-color="#000" stop-opacity="1"/>
      <stop offset="1" stop-color="#000" stop-opacity="0"/>
    </linearGradient>
    <linearGradient id="panel-fill" x1="0" y1="0" x2="0" y2="1">
      <stop offset="0" stop-color="#121212"/>
      <stop offset="0.15" stop-color="#181818"/>
      <stop offset="1" stop-color="#676767"/>
    </linearGradient>
    <linearGradient id="rail-v" x1="0" y1="0" x2="1" y2="0">
      <stop offset="0" stop-color="#3a3a3a"/>
      <stop offset="0.35" stop-color="#cfcfcf"/>
      <stop offset="0.6" stop-color="#8d8d8d"/>
      <stop offset="1" stop-color="#2a2a2a"/>
    </linearGradient>
    <linearGradient id="rail-h" x1="0" y1="0" x2="0" y2="1">
      <stop offset="0" stop-color="#3a3a3a"/>
      <stop offset="0.35" stop-color="#cfcfcf"/>
      <stop offset="0.6" stop-color="#8d8d8d"/>
      <stop offset="1" stop-color="#2a2a2a"/>
    </linearGradient>
    <linearGradient id="small-door-fill" x1="0" y1="0" x2="0" y2="1">
      <stop offset="0" stop-color="#0e0e0e"/>
      <stop offset="0.5" stop-color="#5c5c5c"/>
      <stop offset="1" stop-color="#0e0e0e"/>
    </linearGradient>
    <linearGradient id="chrome" x1="0" y1="0" x2="0" y2="1">
      <stop offset="0" stop-color="#1a1a1a"/>
      <stop offset="0.42" stop-color="#f8f8f8"/>
      <stop offset="0.55" stop-color="#b5b5b5"/>
      <stop offset="1" stop-color="#0c0c0c"/>
    </linearGradient>
    <linearGradient id="chrome-rim" x1="0" y1="0" x2="1" y2="1">
      <stop offset="0" stop-color="#222"/>
      <stop offset="0.5" stop-color="#eee"/>
      <stop offset="1" stop-color="#111"/>
    </linearGradient>
    <linearGradient id="chrome-inner" x1="0" y1="0" x2="0" y2="1">
      <stop offset="0" stop-color="#0e0e0e"/>
      <stop offset="0.5" stop-color="#eaeaea"/>
      <stop offset="0.62" stop-color="#bdbdbd"/>
      <stop offset="1" stop-color="#161616"/>
    </linearGradient>
    <linearGradient id="slot-wall" x1="0" y1="0" x2="1" y2="0">
      <stop offset="0" stop-color="#0a0a0a"/>
      <stop offset="0.5" stop-color="#3a3a3a"/>
      <stop offset="1" stop-color="#d0d0d0"/>
    </linearGradient>
    <linearGradient id="slot-floor" x1="0" y1="0" x2="0" y2="1">
      <stop offset="0" stop-color="#e0e0e0"/>
      <stop offset="1" stop-color="#555"/>
    </linearGradient>
    <radialGradient id="led-green" cx="0.4" cy="0.35" r="0.7">
      <stop offset="0" stop-color="#c8ffb0"/>
      <stop offset="0.45" stop-color="var(--glow-green)"/>
      <stop offset="1" stop-color="#087008"/>
    </radialGradient>
    <radialGradient id="led-red" cx="0.4" cy="0.35" r="0.7">
      <stop offset="0" stop-color="#ffc0b0"/>
      <stop offset="0.45" stop-color="var(--glow-red)"/>
      <stop offset="1" stop-color="#700606"/>
    </radialGradient>
    <filter id="lock-shadow" x="-20%" y="-20%" width="140%" height="140%">
      <feDropShadow dx="3" dy="4" stdDeviation="3" flood-color="#000" flood-opacity="0.7"/>
    </filter>

    <g id="lock-face">
      <circle r="100" fill="url(#chrome)" stroke="#000" stroke-width="2"/>
      <circle r="96" fill="none" stroke="url(#chrome-rim)" stroke-width="3" opacity="0.6"/>
      <circle r="79" fill="#1a1a1a"/>
      <circle r="77" fill="url(#chrome-rim)"/>
      <circle r="73" fill="url(#chrome-inner)"/>
      <rect x="-16" y="-44" width="32" height="88" fill="#0a0a0a"/>
      <rect x="-12" y="-40" width="24" height="80" fill="url(#slot-wall)"/>
      <path d="M-12 -40 L-4 -30 L-4 40 L-12 40 Z" fill="#050505"/>
      <path d="M-4 24 L12 30 L12 40 L-4 40 Z" fill="url(#slot-floor)" opacity="0.8"/>
      <circle cx="-42" r="19" fill="#0a0a0a"/>
      <circle cx="42" r="19" fill="#0a0a0a"/>
    </g>
  </defs>

  <!-- Wall -->
  <rect class="wall" width="1200" height="900" fill="url(#wall-sheen)"/>
  <rect class="wall-shade" width="1200" height="900" fill="url(#wall-fade)"/>

  <!-- Main doors -->
  <g class="main-doors">
    <rect x="59" y="44" width="1083" height="812" fill="#2a2a2a"/>
    <!-- left door frame -->
    <rect x="60" y="45" width="540" height="810" fill="url(#rail-h)"/>
    <rect x="60" y="45" width="14" height="810" fill="url(#rail-v)"/>
    <rect x="584" y="45" width="16" height="810" fill="url(#rail-v)"/>
    <rect class="door-left" x="72" y="62" width="514" height="780" fill="url(#panel-fill)" stroke="#0a0a0a" stroke-width="2"/>
    <line x1="73" y1="843" x2="586" y2="843" stroke="#b0b0b0" stroke-width="2"/>
    <!-- right door frame -->
    <rect x="602" y="45" width="540" height="810" fill="url(#rail-h)"/>
    <rect x="602" y="45" width="16" height="810" fill="url(#rail-v)"/>
    <rect x="1128" y="45" width="14" height="810" fill="url(#rail-v)"/>
    <rect class="door-right" x="618" y="62" width="514" height="780" fill="url(#panel-fill)" stroke="#0a0a0a" stroke-width="2"/>
    <line x1="619" y1="843" x2="1132" y2="843" stroke="#b0b0b0" stroke-width="2"/>
    <rect class="door-seam" x="598" y="45" width="4" height="810" fill="#1a1a1a"/>
    <rect x="60" y="45" width="1082" height="810" fill="none" stroke="#1a1a1a" stroke-width="2"/>
  </g>

  <!-- Main lock -->
  <g class="lock-main" transform="translate(600 440) scale(1.2)" filter="url(#lock-shadow)">
    <use href="#lock-face"/>
    <circle cx="-42" r="14" fill="url(#led-green)"/>
    <circle cx="42" r="14" fill="url(#led-green)"/>
  </g>

  <!-- Component tray -->
  <rect class="component-tray" x="20" y="580" width="1160" height="298" fill="var(--tray)"/>

  <g class="component-doors">
    <rect x="60" y="617" width="158" height="238" fill="#9a9a9a"/>
    <rect x="63" y="620" width="152" height="232" fill="url(#small-door-fill)" stroke="#000" stroke-width="1.5"/>
    <rect x="278" y="617" width="158" height="238" fill="#9a9a9a"/>
    <rect x="281" y="620" width="152" height="232" fill="url(#small-door-fill)" stroke="#000" stroke-width="1.5"/>
    <path d="M218 698 A34 34 0 0 0 218 766 Z" fill="url(#chrome-inner)" stroke="#111" stroke-width="1"/>
    <circle cx="277" cy="732" r="35" fill="url(#chrome)" stroke="#111" stroke-width="2"/>
    <circle cx="277" cy="732" r="28" fill="#1a1a1a"/>
    <circle cx="277" cy="732" r="26" fill="url(#chrome-inner)"/>
  </g>

  <g class="lock-open" transform="translate(530 681) scale(0.53)" filter="url(#lock-shadow)">
    <use href="#lock-face"/>
    <circle cx="-42" r="14" fill="url(#led-green)"/>
    <circle cx="42" r="14" fill="url(#led-green)"/>
  </g>

  <g class="lock-closed" transform="translate(530 801) scale(0.53)" filter="url(#lock-shadow)">
    <use href="#lock-face"/>
    <circle cx="-42" r="14" fill="url(#led-red)"/>
    <circle cx="42" r="14" fill="url(#led-red)"/>
  </g>
</svg>
</body>
</html>
```